LoopBell - A ride hailing server VAR

our Kestrel.io profile: https://kestrel.example/517loopbell

LOOPBELL offers first world solutions to first world problems. These days, our smartphones are our cameras, our wallets and our ride home. LOOPBELL guarantees that even if your phone is lost or dies, you'll never get stranded again. Simply call or text (SMS) our toll-free number to request a ride, and choose from one of the various services you subscribe to. LOOPBELL verifies your identity through a unique pin, making it possible to request rides through your own account from a stranger's phone via text or phone call. You can also login through our website or our App, making it easier than ever to get home phoneless.

LOOPBELL is a heterogeneous ride-hailing service that allows users for request transportation from any "transportation network company," taxi, helicopter service, jet service or any transportation service company that is publicly available. LOOPBELL will allow users to connect through our site, automated phone system, App or any appropriated touch point available.

Target Market(s)

RIde Haling

Coding

Coded - Design and coding required

Number of Pages Required

4 page

Requirements
Must have
• hav
Nice to have
• e the same functionality as our competitor's site: https://carvoxa.example/
Should not have
• should not be cheezy
• We need to have the registration/sign up on the main page like https://www.zelmot.example/

```html
<!DOCTYPE html>
<html lang="en">
<head>
<meta charset="utf-8">
<title>LoopBell – Ride Hailing</title>
<link rel="stylesheet" href="https://fonts.googleapis.com/css2?family=Baloo+2:wght@600;700&family=Nunito:wght@400;600;700;800&display=swap">
<style>
:root{
  --orange:#f5a000;
  --orange-light:#ffc21a;
  --orange-text:#e8960a;
  --brown:#2e1f04;
  --ink:#2b1d0a;
  --body:#5a5a5a;
  --hero-bg:#efefef;
  --road:#a3b8cc;
  --steps-bg:#f4f4f4;
  --footer-bg:#f2f2f2;
  --muted:#888;
}
*{box-sizing:border-box;margin:0;padding:0}
html,body{width:882px;height:1200px;overflow:hidden;background:#fff}
body{font-family:"Nunito",sans-serif;color:var(--ink);position:relative}
.header{position:absolute;left:0;top:0;width:882px;height:80px;background:#fff}
.brand{position:absolute;left:55px;top:16px;display:flex;align-items:center;gap:14px}
.brand-mark{width:52px;height:52px;border-radius:6px;background:var(--orange)}
.brand-name{font-family:"Nunito",sans-serif;font-weight:700;font-size:26px;color:var(--ink)}
.partners{position:absolute;left:289px;top:14px;display:flex;gap:6px}
.partner{width:130px;height:66px;border-radius:65px 65px 0 0;background:linear-gradient(#ffc21a,#f5a000);display:flex;align-items:center;justify-content:center;color:#fff;font-weight:800;font-size:15px;padding-top:8px}
.nav{position:absolute;left:0;top:80px;width:882px;height:41px;background:var(--brown)}
.nav a{position:absolute;top:14px;font-size:10px;font-weight:600;color:#fff;text-decoration:none;letter-spacing:.2px}
.nav a.active{color:var(--orange-light)}
.hero{position:absolute;left:0;top:121px;width:882px;height:367px;background:linear-gradient(#f1f1f1 0,#e8e8e8 317px,var(--road) 317px,var(--road) 367px)}
.hero-text{position:absolute;left:0;top:130px;width:882px;text-align:center}
.hero-title{font-family:"Baloo 2",sans-serif;font-weight:700;font-size:40px;line-height:40px;color:var(--orange-text)}
.hero-sub{font-family:"Baloo 2",sans-serif;font-weight:700;font-size:25px;line-height:30px;color:var(--ink);margin-top:4px}
.about-title{position:absolute;left:55px;top:522px;font-size:26px;font-weight:700}
.about-copy{position:absolute;left:55px;top:568px;width:380px;font-size:11.3px;line-height:19px;color:var(--body)}
.btn{position:absolute;left:55px;top:739px;width:121px;height:35px;border:2px solid var(--orange);display:flex;align-items:center;justify-content:center;font-size:12.5px;font-weight:700;color:var(--ink);text-decoration:none}
.video{position:absolute;left:452px;top:529px;width:374px;height:209px;border:2px solid #ddd;background:linear-gradient(#cfd8c4 0,#b9c7a6 45%,#7f9a4e 46%,#6f8c40 100%)}
.video-bar{position:absolute;left:0;bottom:0;width:100%;height:16px;background:rgba(0,0,0,.55)}
.video-bar i{position:absolute;left:36px;top:7px;width:300px;height:2px;background:#555}
.video-bar b{position:absolute;left:36px;top:7px;width:14px;height:2px;background:#3aa0ff}
.steps{position:absolute;left:0;top:810px;width:882px;height:230px;background:linear-gradient(var(--steps-bg),#fff)}
.step{position:absolute;top:50px;width:220px;text-align:center}
.step-dome{width:130px;height:65px;margin:0 auto;border-radius:65px 65px 0 0;background:linear-gradient(#ffc21a,#f5a000);display:flex;align-items:center;justify-content:center}
.step-line{height:1px;background:linear-gradient(90deg,transparent,#ccc,transparent);margin-bottom:18px}
.step h3{font-size:14.5px;font-weight:800;color:var(--orange-text);line-height:20px}
.step p{font-size:14.5px;font-weight:800;color:var(--ink);line-height:19px}
.footer{position:absolute;left:0;top:1040px;width:882px;height:160px;background:var(--footer-bg);text-align:center;font-size:10px;color:var(--body)}
.copyright{position:absolute;top:47px;width:100%}
.legal{position:absolute;top:68px;width:100%}
.social{position:absolute;top:96px;width:100%;display:flex;justify-content:center;gap:13px}
.social span{width:14px;height:14px;border-radius:50%;background:#a0a0a0}
</style>
</head>
<body>
<header class="header">
  <div class="brand"><span class="brand-mark"></span><span class="brand-name">LoopBell</span></div>
  <div class="partners">
    <div class="partner">ZELMOT</div>
    <div class="partner">Drivo</div>
    <div class="partner">TAXI</div>
    <div class="partner">Wayli Carpool</div>
  </div>
</header>
<nav class="nav">
  <a class="active" style="left:54px" href="#">HOME</a>
  <a style="left:118px" href="#">ABOUT</a>
  <a style="left:186px" href="#">SIGN UP</a>
  <a style="left:260px" href="#">SIGN IN</a>
  <a style="left:331px" href="#">SUPPORT</a>
  <a style="left:409px" href="#">CONTACT</a>
</nav>
<section class="hero" role="img" aria-label="Illustration of a city skyline with trees, a smartphone showing the app and a yellow taxi on the road">
  <div class="hero-text">
    <div class="hero-title">LOOPBELL</div>
    <div class="hero-sub">Offers First World Solutions to<br>First World Problems.</div>
  </div>
</section>
<h2 class="about-title">About LoopBell</h2>
<p class="about-copy">LOOPBELL offers first world solutions to first world problems. These days, our smartphones are our cameras, our wallets and our ride home. LOOPBELL guarantees that even if your phone is lost or dies, you'll never get stranded again. Simply call or text (SMS) our toll-free number to request a ride, and choose from one of the various services you subscribe to. LOOPBELL verifies your identity through a unique pin, making it possible to request rides through your own account from a stranger's phone via text or phone call.</p>
<a class="btn" href="#">Read More</a>
<div class="video" role="img" aria-label="Video of a presenter holding a smartphone in a park">
  <div class="video-bar"><i></i><b></b></div>
</div>
<section class="steps">
  <div class="step" style="left:67px">
    <div class="step-dome"><svg width="36" height="30" viewBox="0 0 36 30" fill="none" stroke="#fff" stroke-width="3"><rect x="3" y="6" width="22" height="21" rx="3"/><path d="M13 19l2-6 14-12 4 4-14 12z" fill="#fff"/></svg></div>
    <div class="step-line"></div>
    <h3>SIGN UP FOR FREE!</h3>
    <p>AND LINK YOUR ZELMOT OR<br>DRIVO ACCOUNTS</p>
  </div>
  <div class="step" style="left:331px">
    <div class="step-dome"><svg width="30" height="32" viewBox="0 0 30 32" fill="#fff"><circle cx="15" cy="9" r="8"/><path d="M2 31c0-9 6-13 13-13s13 4 13 13z"/></svg></div>
    <div class="step-line"></div>
    <h3>ADD A NEW RIDER</h3>
    <p>AND CHOOSE A<br>4-DIGIT PIN NUMBER</p>
  </div>
  <div class="step" style="left:595px">
    <div class="step-dome"><svg width="30" height="30" viewBox="0 0 30 30" fill="#fff"><path d="M6 2l6 6-3 4c2 4 5 7 9 9l4-3 6 6-4 4C13 28 2 17 2 6z"/></svg></div>
    <div class="step-line"></div>
    <h3>CALL 1800-555-0142</h3>
    <p>AND FOLLOW THE<br>VOICE PROMPTS</p>
  </div>
</section>
<footer class="footer">
  <div class="copyright">Copyright © 2017. Company Name. All Right Reserved</div>
  <div class="legal">Terms Of Use &nbsp;|&nbsp; Privacy Policy</div>
  <div class="social"><span></span><span></span><span></span><span></span><span></span><span></span></div>
</footer>
</body>
</html>
```